Vordaline - Fitness Coach. Needs a Business Card Design that I can also use for other advertising

Established 2012, I have finished the KTRB National Certificate in Fitness & Personal Training. Harlow Cross First Aid Certificate. I have the Auckland 800m track records for MW45. I also came 1st at the 2012 Pellamar Games in 800 & 1500m. I am passionate about health & fitness and would like to help people reach their health & fitness goals. I also take health & fitness weekends. Main interests - Running, Weight Training, Yoga & Aqua Jogging. I like strength/power, but am femine.

Target Market(s)

Male or Female 18 and over that wants to improve their health & fitness

Industry/Entity Type

Advertising

Requirements
Must have
• my name: Rosalind K Tarbury contact details: ros@quillsend.co.nz mobile - 021 583917 URL name: facebook.com/rosalindKtarbury - VordaLine
Photo of Me

```html
<!DOCTYPE html>
<html lang="en">
<head>
<meta charset="utf-8">
<title>Rosalind K Tarbury – Vordaline Fitness Coach</title>
<link rel="stylesheet" href="https://fonts.googleapis.com/css2?family=Open+Sans:wght@400&display=swap">
<style>
  :root {
    --paper: #ffffff;
    --panel-top: #ffffff;
    --panel-bottom: #eeeeee;
    --panel-edge: rgba(0, 0, 0, 0.10);
    --frame: #f4f4f4;
    --frame-line: #e2e2e2;
    --foliage-dark: #1f3f12;
    --foliage: #3d7a1f;
    --lawn: #5fbf1e;
    --accent: #2bd11a;
    --ink: #111111;
    --rule: #cfcfcf;
  }
  html, body {
    margin: 0;
    padding: 0;
    overflow: hidden;
    background: var(--paper);
  }
  .card {
    position: relative;
    width: 1200px;
    height: 836px;
    overflow: hidden;
    background: var(--paper);
    font-family: "Open Sans", sans-serif;
  }
  .portrait-frame {
    position: absolute;
    left: 52px;
    top: 50px;
    width: 444px;
    height: 734px;
    background: var(--frame);
    border: 1px solid var(--frame-line);
  }
  .portrait {
    position: absolute;
    left: 14px;
    top: 14px;
    width: 416px;
    height: 706px;
    background: linear-gradient(180deg,
      var(--foliage-dark) 0%,
      var(--foliage) 45%,
      var(--foliage-dark) 72%,
      var(--lawn) 76%,
      var(--lawn) 100%);
  }
  .contact-panel {
    position: absolute;
    left: 581px;
    top: 0;
    width: 619px;
    height: 836px;
    background: linear-gradient(180deg, var(--panel-top) 0%, var(--panel-top) 30%, var(--panel-bottom) 100%);
  }
  .contact-panel::before {
    content: "";
    position: absolute;
    left: -28px;
    top: 0;
    width: 28px;
    height: 100%;
    background: linear-gradient(90deg, rgba(0,0,0,0) 0%, var(--panel-edge) 100%);
  }
  .contact {
    position: absolute;
    left: 52px;
    top: 266px;
    margin: 0;
    color: var(--ink);
    font-size: 47px;
    line-height: 70px;
    font-weight: 400;
  }
  .contact-name {
    display: block;
    color: var(--accent);
    padding-bottom: 6px;
    margin-bottom: 2px;
    border-bottom: 3px dashed var(--rule);
    width: 454px;
    line-height: 60px;
  }
  .contact-line {
    display: block;
    white-space: nowrap;
  }
</style>
</head>
<body>
  <div class="card">
    <div class="portrait-frame">
      <div class="portrait" role="img" aria-label="Photo of the coach leaping in the air in an orange top and dark leggings in front of a leafy green hedge over a lawn"></div>
    </div>
    <section class="contact-panel">
      <p class="contact">
        <span class="contact-name">Rosalind K Tarbury</span>
        <span class="contact-line">ros@quillsend.co.nz</span>
        <span class="contact-line">Call me - 021 583917</span>
        <span class="contact-line">linkspace - Vordaline</span>
      </p>
    </section>
  </div>
</body>
</html>
```